Business Card Design

It's an investment advisory service for individuals with all there investment needs. Also financial consulting to businesses and governmental agencies on retirement plans etc. It's personalized not commoditized help. Should show strength, knowledge and money orientation.
Updates

Reason: Will be out of town setting up office.

Reason: waiting for the 2/3rds of group to vote

Reason: only half the votes are in, I'm calling and getting verbals, but at this time we are down to 2 designs.

Industry/Entity Type

Investment

Contact Information for Business Card

B. Rel K. Financial Consulting and Wealth Management, Desmond Wick Harlow, 5172 Paseo Loma Verde Crest, San Diego, CA 92131-4817, Registered Investment Advisor

Requirements
Nice to have
• Something money oriented

```html
<!DOCTYPE html>
<html lang="en">
<head>
<meta charset="utf-8">
<title>B. Rel K. Financial Consulting and Wealth Management – Business Card</title>
<link rel="stylesheet" href="https://fonts.googleapis.com/css2?family=Cantarell:wght@400;700&display=swap">
<style>
  :root {
    --panel-light: #687260;
    --panel-dark: #464f40;
    --edge-shadow: #3c4436;
    --firm-text: #c2c5bd;
    --ink: #121510;
  }
  html, body {
    margin: 0;
    padding: 0;
    width: 1200px;
    height: 702px;
    overflow: hidden;
    background: var(--panel-dark);
  }
  .card {
    position: relative;
    width: 1200px;
    height: 702px;
    overflow: hidden;
    font-family: "Cantarell", sans-serif;
  }
  .card-background {
    position: absolute;
    inset: 0;
    width: 1200px;
    height: 702px;
  }
  .firm-name,
  .advisor,
  .contact {
    position: absolute;
    margin: 0;
    line-height: 1;
    white-space: nowrap;
  }
  .firm-name {
    left: 0;
    top: 0;
    width: 592px;
    height: 702px;
    text-align: center;
    color: var(--firm-text);
    font-weight: 400;
  }
  .firm-initials {
    position: absolute;
    left: 0;
    width: 100%;
    top: 238px;
    font-size: 58px;
    letter-spacing: 1px;
  }
  .firm-line {
    position: absolute;
    left: 0;
    width: 100%;
    font-size: 40px;
    letter-spacing: 1.2px;
  }
  .firm-line--first { top: 309px; }
  .firm-line--second { top: 360px; }
  .firm-line--third { top: 412px; }

  .advisor {
    left: 642px;
    width: 500px;
    top: 0;
    text-align: center;
    color: var(--ink);
  }
  .advisor-name {
    position: absolute;
    left: 0;
    width: 100%;
    top: 302px;
    font-size: 42px;
    font-weight: 700;
    letter-spacing: 0.5px;
  }
  .advisor-title {
    position: absolute;
    left: 0;
    width: 100%;
    top: 354px;
    font-size: 35px;
    font-weight: 400;
    letter-spacing: 0.8px;
  }

  .contact {
    right: 61px;
    top: 590px;
    text-align: right;
    color: var(--ink);
    font-size: 26px;
    letter-spacing: 1px;
  }
  .contact-phones { display: block; height: 30px; }
  .contact-phones span + span { margin-left: 30px; }
  .contact-email { display: block; }
</style>
</head>
<body>
  <main class="card">
    <svg class="card-background" viewBox="0 0 1200 702" aria-hidden="true">
      <defs>
        <linearGradient id="edge-fade" x1="0" y1="0" x2="1" y2="0">
          <stop offset="0" stop-color="var(--edge-shadow)" stop-opacity="0.55"/>
          <stop offset="1" stop-color="var(--edge-shadow)" stop-opacity="0"/>
        </linearGradient>
      </defs>
      <rect width="1200" height="702" fill="var(--panel-dark)"/>
      <polygon points="639,0 653,0 521,702 507,702" fill="url(#edge-fade)"/>
      <polygon points="0,0 639,0 507,702 0,702" fill="var(--panel-light)"/>
    </svg>

    <h1 class="firm-name">
      <span class="firm-initials">B. Rel K.</span>
      <span class="firm-line firm-line--first">Financial Consulting</span>
      <span class="firm-line firm-line--second">and</span>
      <span class="firm-line firm-line--third">Wealth Management</span>
    </h1>

    <div class="advisor">
      <p class="advisor-name">Desmond Wick Harlow</p>
      <p class="advisor-title">Registered Investment Advisor</p>
    </div>

    <address class="contact" style="font-style: normal;">
      <span class="contact-phones"><span>858-555-0142</span><span>775-555-0187</span></span>
      <span class="contact-email">d.harlow@harlowmail.com</span>
    </address>
  </main>
</body>
</html>
```